CODED website - Wanderfrom418

I am a successful entrepreneur - have recently sold my business and am semi-retired. I want to give something back, as well as provide a blog for articles and my journeys.

I will also be using this to provide free business and entrepreneurial advice.

I am creating a NOT FOR PROFIT business called Wanderfrom418.com.au which will provide the following;

1. Blog and articles; my travels, Small to Medium business advice and articles

2. My Bucket List - the 100 things I aim to achieve

3. Free business / start up advice - a section on the website which provides case studies on people / businesses which ask me for advice. We will then chronicle their story and what advice we have given for them to succeed.

My inspiration is the Marten Oskoby idea and website;

http://martenoskoby.com/about-marten/

Obviously I do NOT want a copy of this site, but use this for inspiration.

Furthermore, I would be interested in ongoing collaboration with the successful designer - I will be providing advice and consultancy to start ups, all of which will need web design etc, so there is ongoing referral streams for the successful designer.

I need this to be CODED and then uplifted to the website, so please DO NOT bid on this unless you can provide a coded site and facilitate the upload to BrightHostly.

The NECESSARY tabs / pages

Main landing page - a short introduction into the ethos of Wanderfrom418

Writing - this will be the blog articles

About

Our Bucket List - a section where we can add our 100 buket list items. Hyperlinked to open a new page which has details on each bucket list item (ie #1 Make Wanderfrom418 - hyperlink to a new page which then has info on the bucklist item and what we have done)

Wanderfrom418 - this will be the section where we discuss people / businesses that we are helping. We will have an opening intro section + a link to the contact us page so they can ask us for the free advice. This will be the section where we have case studies into businesses / people that we have helped.

Hey everyone!

I'm really keen to get this website launched and looking amazing - if you have any questions, or would like to discuss anything at all, please email me at

dane@pellorpost.com.au

As I mentioned in the brief, I am doing this site to give back; I will not be earning a cent, and I will not be trying to earn any funds. I'm doing it simply to help other start ups or entrepreneurs, so I really want this site to look amazing.

I hope someone reads this and is inspired, and wants to be involved in this social enterprise with me.

Really excited to hear from you all and see your designs!

Industry/Entity Type

Business

Requirements
Must have
• MUST BE CODED and uplifted to the BrightHostl registered domain - www.wanderfrom418.com.au - happy to discuss additional costings for this with successful designer.

Separate pages for each section (as outlined in the brief above)

Blog section to look similar to http://martenoskoby.com/3x5/

Comprehensive website - not a simple wordpress template theme with some minor modifications. I will immediately reject any simple template design. I am looking for a slick, fully functioning website design.

PLEASE BE AWARE that I am looking for ongoing collaboration with the www.wanderfrom418.com.au.

I am trying this website as I want to find a young, energetic, vibrant, dynamic designer - this is your opportunity to be a part of something big, as this website will be huge!

Please do not submit a design if you are not motivated and ready for something big.

```html
<!DOCTYPE html>
<html lang="en">
<head>
<meta charset="utf-8">
<title>Wanderfrom418</title>
<link rel="stylesheet" href="https://fonts.googleapis.com/css2?family=Arimo:wght@400;700&family=Barlow:wght@300;400&family=Bree+Serif&display=swap">
<style>
:root{
  --sand:#d9cd98;
  --sand-dark:#cfc28a;
  --sand-line:#ece4bf;
  --paper:#fdfdfa;
  --paper-edge:#e9e6cf;
  --ink:#333;
  --teal:#1f8686;
  --teal-band:#6aaab0;
  --olive:#6a6344;
  --olive-soft:#76704f;
  --muted:#888;
  --button:#c9bd80;
  --widget-accent:#2f4a78;
  --frame:#e6e6e2;
  --photo:#5b4234;
}
*{margin:0;padding:0;box-sizing:border-box}
html,body{width:1200px;height:792px;overflow:hidden}
body{position:relative;background:linear-gradient(180deg,#ddd3a4 0,var(--sand) 440px,var(--sand-dark) 792px);font-family:Arimo,Arial,sans-serif;color:var(--ink)}
.abs{position:absolute}

.content-panel{position:absolute;left:137px;top:0;width:929px;height:425px;background:var(--paper);border:1px solid var(--paper-edge);border-top:none;box-shadow:0 0 0 6px rgba(240,236,210,.6)}
.panel-divider{position:absolute;left:786px;top:0;width:2px;height:408px;background:#ddd7b8}

.intro-text{left:164px;top:-5px;font-size:12.5px;line-height:18px;white-space:nowrap}
.intro-text a{color:var(--teal)}
.section-title{left:164px;top:99px;font-family:"Bree Serif",Georgia,serif;font-size:18.5px;font-weight:400;color:var(--teal)}
.lead-text{left:164px;top:137px;font-size:12px;line-height:18px;font-weight:700;color:var(--teal);white-space:nowrap}

.carousel-arrow{top:262px;font-size:32px;color:#c9bd80;font-family:Arimo,sans-serif;line-height:1}
.photo-frame{top:211px;width:140px;height:142px;background:var(--frame);border:1px solid #f4f4f2;box-shadow:0 1px 3px rgba(0,0,0,.18)}
.photo-frame .photo{position:absolute;left:10px;top:10px;width:118px;height:120px;background:radial-gradient(circle at 50% 40%,#8a6047,var(--photo) 60%,#2c231f)}

.post-thumb{left:802px;top:12px;width:40px;height:40px;background:linear-gradient(#7f8d9c,#b88a6c);border:1px solid #ccc}
.post-title{left:853px;top:6px;width:200px;font-size:14px;line-height:16px;color:var(--teal)}
.post-meta{left:853px;top:40px;font-size:11px;color:var(--muted)}
.read-more{left:801px;top:73px;width:105px;height:26px;background:var(--button);border:1px solid #b7ab6d;color:#fff;font-size:15px;text-align:center;line-height:24px}

.social-band{left:787px;top:128px;width:279px;height:35px;background:var(--teal-band);border-top:2px dashed #9fcdd0;border-bottom:2px dashed #9fcdd0;color:#fff;font-family:Barlow,sans-serif;font-weight:400;font-size:19px;letter-spacing:.5px;padding:6px 0 0 23px}

.social-box{left:809px;top:185px;width:233px;height:186px;background:#fff;border:1px solid #aaa}
.social-box .page-mark{position:absolute;left:8px;top:11px;width:48px;height:40px;background:#dfe7df}
.social-box .page-name{position:absolute;left:60px;top:11px;font-size:14px;font-weight:700;color:var(--widget-accent)}
.social-box .like-btn{position:absolute;left:60px;top:30px;width:47px;height:23px;border:1px solid #b6c2dc;background:#eef1f8;font-size:10px;color:var(--widget-accent);line-height:21px;padding-left:20px}
.social-box .rule{position:absolute;left:6px;width:220px;height:1px;background:#ddd}
.social-box .count{position:absolute;left:10px;top:69px;font-size:10px;color:#333}
.social-box .count b{color:var(--widget-accent);font-size:12px;margin-left:4px}
.social-box .fan{position:absolute;top:90px;width:49px;height:49px;background:linear-gradient(#9a938a,#5a4c44)}
.social-box .fan-name{position:absolute;top:146px;width:55px;text-align:center;font-size:9px;color:#666}
.social-box .plugin{position:absolute;left:8px;top:165px;font-size:9px;color:#555;display:flex;align-items:center;gap:6px}
.social-box .plugin i{width:13px;height:13px;background:var(--widget-accent);display:block}

.footer-rule{position:absolute;left:128px;width:948px;height:1px;background:var(--sand-line)}
.footer-heading{top:494px;font-family:Barlow,sans-serif;font-weight:400;font-size:24px;letter-spacing:1px;color:var(--olive)}
.footer-list{list-style:none;top:537px;font-size:14px;color:var(--olive-soft)}
.footer-list li{height:30px;display:flex;align-items:flex-start;gap:13px}
.footer-list svg{width:10px;height:10px;margin:5px 0 0 1px}
.contact{left:861px;top:537px;font-size:14px;color:var(--olive-soft);line-height:20px}
.contact a{color:var(--olive);text-decoration:underline}
.contact .label{font-weight:700;font-size:16px;color:var(--olive);margin-top:15px}
.contact .address{margin-top:3px}
.bottom-nav{left:138px;top:752px;font-size:13px;color:var(--olive-soft);display:flex}
.bottom-nav span{margin-right:32px}
.copyright{right:143px;top:753px;font-size:13px;color:var(--olive-soft)}
</style>
</head>
<body>
<svg width="0" height="0" style="position:absolute">
  <symbol id="bullet" viewBox="0 0 10 10"><path d="M5 0v10M0 5h10M3.5 1.5 5 0l1.5 1.5M3.5 8.5 5 10l1.5-1.5M1.5 3.5 0 5l1.5 1.5M8.5 3.5 10 5 8.5 6.5" stroke="#6a6344" stroke-width="1" fill="none"/></symbol>
</svg>

<div class="content-panel"></div>
<div class="panel-divider"></div>

<p class="abs intro-text">Morbi ut mi. Nullam enim leo, egestas id, condimentum at, laoreet. Lorem Ipsum Text.<br><br>Lorem <a href="#">ipsum dolor sit amet, consectetuer adipiscing elit</a>. Nam cursus. Morbi ut mi. Nullam enim &nbsp;leo,<br>egestas id, condimentum at, laoreet. Lorem Ipsum Text. Lorem ipsum dolor sit amet, consectetuer adipisc<br>ing elit. Nam cursus. Morbi ut mi. Nullam enim leo, egestas id, condimentum at, laoreet.</p>
<h2 class="abs section-title">Loren ipsum is simply</h2>
<p class="abs lead-text">Lorem Ipsum Text. Lorem ipsum dolor sit amet, consectetuer adipiscing elit. Nam cursus. Morbi ut<br>mi. dfdff Nullam enim leo, egestas id, condimentum at, laoreet. Lorem Ipsum Text.</p>

<span class="abs carousel-arrow" style="left:165px">&#10094;</span>
<div class="abs photo-frame" style="left:202px"><div class="photo" role="img" aria-label="Portrait photo of a smiling woman"></div></div>
<div class="abs photo-frame" style="left:389px"><div class="photo" role="img" aria-label="Portrait photo of a smiling woman"></div></div>
<div class="abs photo-frame" style="left:572px"><div class="photo" role="img" aria-label="Portrait photo of a smiling woman"></div></div>
<span class="abs carousel-arrow" style="left:736px">&#10095;</span>

<div class="abs post-thumb" role="img" aria-label="Author photo"></div>
<p class="abs post-title">Lorem ipsum all time favorite personal finance book!</p>
<p class="abs post-meta">Jan 03, 2013. by admin</p>
<div class="abs read-more">Read More</div>

<div class="abs social-band">FIND US ON FRIENDWALL</div>
<div class="abs social-box">
  <div class="page-mark"></div>
  <div class="page-name">Wander from 418</div>
  <div class="like-btn">Like</div>
  <div class="rule" style="top:62px"></div>
  <div class="count">15,073 people like<b>Wander from 418</b></div>
  <div class="fan" style="left:10px" role="img" aria-label="Fan photo"></div>
  <div class="fan" style="left:65px" role="img" aria-label="Fan photo"></div>
  <div class="fan" style="left:120px" role="img" aria-label="Fan photo"></div>
  <div class="fan" style="left:172px" role="img" aria-label="Fan photo"></div>
  <div class="fan-name" style="left:7px">Orlan</div>
  <div class="fan-name" style="left:62px">Tvmaneesh</div>
  <div class="fan-name" style="left:117px">Odimbu</div>
  <div class="fan-name" style="left:170px">Marguerite</div>
  <div class="rule" style="top:161px"></div>
  <div class="plugin"><i></i>Friendwall social plugin</div>
</div>

<div class="footer-rule" style="top:467px"></div>
<h3 class="abs footer-heading" style="left:136px">ARCHIVES</h3>
<h3 class="abs footer-heading" style="left:488px">QUICK LINKS</h3>
<h3 class="abs footer-heading" style="left:859px">CONTACT US</h3>

<ul class="abs footer-list" style="left:136px">
  <li><svg><use href="#bullet"/></svg>May 2012</li>
  <li><svg><use href="#bullet"/></svg>April 2012</li>
  <li><svg><use href="#bullet"/></svg>March 2012</li>
  <li><svg><use href="#bullet"/></svg>February 2012</li>
  <li><svg><use href="#bullet"/></svg>January 2012</li>
  <li><svg><use href="#bullet"/></svg>December 2012</li>
</ul>
<ul class="abs footer-list" style="left:487px">
  <li><svg><use href="#bullet"/></svg>Lorem ispum is</li>
  <li><svg><use href="#bullet"/></svg>Simply dummy text</li>
  <li><svg><use href="#bullet"/></svg>Here for web and print</li>
  <li><svg><use href="#bullet"/></svg>Lorem ipsum is simply</li>
  <li><svg><use href="#bullet"/></svg>Simply dummy text</li>
  <li><svg><use href="#bullet"/></svg>Lorem ipsum is simply</li>
</ul>
<div class="abs contact">
  <p>Tel: 555 214 0937</p>
  <p style="margin-top:10px">Email: <a href="#">info@ipsum.com</a></p>
  <p class="label">Address:</p>
  <p class="address">14 Hollin Lane<br>Brackley<br>Northamshire<br>NN 13 7QR</p>
</div>

<div class="footer-rule" style="top:736px"></div>
<nav class="abs bottom-nav"><span>About Us</span><span>Place</span><span>Writing</span><span>Store</span><span>Contact</span></nav>
<p class="abs copyright">Copyright © 2012-2013 Wanderfrom418.com.au</p>
</body>
</html>
```